Radical T-shirt Company Shopify Site

I would like to have a a Shopify site designed (and built) for my new t-shirt company. The company is called Zip Tribe and will feature t-shirt designs focused on different characters doing extreme sports. The brand has a mellow and slightly comical feel. We will feature different artists designs as different collections of the brand.
We do not have a logo yet, but we do have some of the sample designs from the artists that we will be featuring on the site. This will give a feel for the branding and style of the site. As far as colors go, I am not sure if a dark theme or light theme will be best. Please use your best judgement for initial designs. Our t-shirt designs are simple and typically line-art style.
It is important to keep in mind that we have several artists that we will feature and that we want to showcase all of them equally until we can understand which will be most popular. Our sites should speak to audiences of all ages. Light, mellow, and slightly comical describe our brand. The site should catch the audiences eye and allow them to see multiple products so they are more likely to buy multiple products.

Expected deliverables:
1. Zip Tribe Gear website (focused on mobile device viewing)- including landing page, multiple collections, product pages, variable colors and sized for shirts and other products, about page, contact page, cart with upsells, subscription package functionality, mailing list pop-up, chat support widget, promo codes, payment collection via stripe- All features should be tested and functioning properly before launch. The site must also be set up to A/B test different products, variations, and upsells.
2. Zip Nana Website (Focused on mobile site viewing) - Should follow the same branding (with a different logo but in the same coloring and style as the Zip Tribe). This should essentially be a copy of the Zip Tribe website include landing page, multiple collections, product pages, variable colors and sized for shirts and other products, about page, contact page, cart with upsells, subscription package functionality, mailing list pop-up, chat support widget, promo codes, payment collection via stripe- Again, this is a duplicate of the Zip Tribe website, but with a different landing page tuned to Zip Nana gear.
3. Coding and development of these sites - with the input of 20-30 products (images, descriptions, pricing provided)

I will provide:
1. Examples of products to help with branding and design of the site
2. Feedback on the site
3. All product information for addition to the site
4. Shopify and plugin credentials or access as needed
5. Ongoing work if this goes well

Looking forward to seeing everyone's designs!

Target Market(s)

People that would wear shirts with our characters; grandmas, grandpas, moms, dads, kids, pet lovers- pretty much anyone who enjoys a bit of humor and a nice shirt.

Industry/Entity Type

Comical yet high end t-shirts

Coding

Coded - Design and coding required

Font styles to use
Sans Serif

Requirements
Must have
• Mobile device optimized, Collections carousel on landing page, upsells, features, other recent order popups for users viewing the site, mailing list popup, coupon codes
Nice to have
• Elegant yet playful feel, branding that instills trust and a quick buy.

```html
<!DOCTYPE html>
<html lang="en">
<head>
<meta charset="utf-8">
<title>Zip Tribe Gear</title>
<link href="https://fonts.googleapis.com/css2?family=Anton&family=Roboto:ital,wght@0,400;0,500;0,700;1,400&display=swap" rel="stylesheet">
<style>
:root{
  --gold:#edbb45;
  --gold-deep:#e9b23a;
  --ink:#222222;
  --text:#444444;
  --muted:#777777;
  --hero-bg:#c9c9c9;
  --white:#ffffff;
  --line:#e6e6e6;
  --chip:#ececec;
}
*{box-sizing:border-box;margin:0;padding:0}
html,body{width:1200px;height:3618px;overflow:hidden;background:var(--white)}
body{position:relative;font-family:'Roboto',sans-serif;color:var(--text)}
.abs{position:absolute}
.display{font-family:'Anton',sans-serif;font-weight:400;letter-spacing:.5px}

/* header + hero */
.hero{left:0;top:0;width:1200px;height:686px;background:linear-gradient(90deg,#bdbdbd 0%,#cfcfcf 55%,#d6d6d6 100%)}
.hero-photo{left:590px;top:84px;width:610px;height:602px;background:radial-gradient(ellipse at 55% 60%,#f2f2f2 0%,#dedede 45%,#cfcfcf 75%)}
.brand{left:111px;top:62px;display:flex;align-items:center;gap:12px;font-weight:700;font-size:22px;color:var(--ink)}
.brand .mark{width:34px;height:34px;border-radius:50%;background:var(--ink)}
.nav{left:377px;top:36px;display:flex;font-size:14px;font-weight:500;color:var(--ink)}
.nav a{color:inherit;text-decoration:none;margin-right:28px;position:relative}
.nav a.active::before{content:"";position:absolute;left:0;right:0;top:-8px;height:2px;background:var(--gold)}
.cart{left:846px;top:30px;display:flex;align-items:center;gap:14px;font-size:14px;color:var(--ink)}
.cart .ico{width:30px;height:30px;border-radius:50%;background:var(--gold);display:flex;align-items:center;justify-content:center}
.login{left:1031px;top:37px;font-size:14px;color:var(--ink);display:flex;align-items:center;gap:6px}
.hero-title{left:111px;top:278px;font-size:54px;color:var(--white);line-height:1.1}
.hero-copy{left:111px;top:352px;width:340px;font-size:14px;line-height:25px;color:var(--white)}
.btn-gold{left:111px;top:417px;width:184px;height:42px;border-radius:21px;background:var(--gold);font-size:14px;font-weight:700;color:var(--ink);display:flex;align-items:center;justify-content:center}
.dots{left:110px;top:586px;display:flex;gap:4px}
.dots span{width:12px;height:12px;border-radius:50%;background:var(--white)}
.dots span:first-child{background:var(--gold)}

/* section titles */
.sec-title{left:0;width:1200px;text-align:center;font-size:56px;color:var(--ink);line-height:1}
.rule{height:3px;width:76px;background:var(--gold)}

/* products */
.card{top:915px;width:313px;height:400px;border:2px solid var(--ink);background:var(--white);overflow:hidden}
.card .shot{position:absolute;left:70px;top:12px;width:170px;height:218px;background:radial-gradient(ellipse at 50% 45%,#ffffff 0%,#f1f1f1 60%,#e6e6e6 100%);border-radius:10px}
.card .name{position:absolute;left:22px;top:236px;font-size:18px;color:var(--ink)}
.card .price{position:absolute;left:22px;top:273px;font-size:21px;font-weight:500;color:var(--gold-deep)}
.card .opt{position:absolute;top:319px;height:43px;background:var(--chip);display:flex;align-items:center;padding-left:16px;font-size:12px;font-weight:700;color:var(--ink)}
.card .opt.color{left:22px;width:124px}
.card .opt.size{left:155px;width:126px}
.card .swatch{position:absolute;right:12px;top:6px;width:30px;height:30px;border-radius:50%;background:var(--white);border:1px solid #d4d4d4}
.card .size-box{position:absolute;right:6px;top:5px;width:40px;height:33px;background:var(--white);display:flex;align-items:center;justify-content:center;font-size:12px}
.card .corner{position:absolute;right:0;bottom:0;width:56px;height:56px}

/* about */
.about{left:0;top:1435px;width:1200px;height:555px;background:var(--gold)}
.about-title{left:111px;top:1540px;font-size:54px;color:var(--white);line-height:1.1}
.about-copy{left:111px;top:1638px;width:482px;font-size:14.5px;line-height:25.7px;color:var(--white);text-align:justify}
.btn-white{background:var(--white);color:var(--ink);font-size:14px;font-weight:700;display:flex;align-items:center;justify-content:center}
.about-frame{left:1012px;top:1530px;width:99px;height:164px;background:var(--white)}
.about-photo{left:631px;top:1552px;width:457px;height:342px;background:linear-gradient(135deg,#9aa49e 0%,#e8e8e8 35%,#f4f4f4 60%,#6d7a8e 100%)}

/* testimonials */
.quote{top:2207px;width:235px;height:318px;background:var(--white);box-shadow:0 0 8px rgba(0,0,0,.12);border-bottom:5px solid var(--gold)}
.quote.alt{border-bottom-color:#cfcfcf}
.quote .qm{position:absolute;left:18px;top:6px;font-family:'Anton',sans-serif;font-size:50px;line-height:1;color:var(--ink)}
.quote .stars{position:absolute;right:20px;top:18px;font-size:15px;color:var(--gold);letter-spacing:2px}
.quote .say{position:absolute;left:20px;top:52px;width:196px;font-style:italic;font-size:14.5px;line-height:25.7px;color:var(--muted);text-align:justify}
.quote .avatar{position:absolute;left:18px;top:244px;width:46px;height:46px;border-radius:50%;background:linear-gradient(#b9b9b9,#8a8a8a)}
.quote .who{position:absolute;left:74px;top:249px;font-size:17px;color:var(--ink)}
.quote .org{position:absolute;left:74px;top:272px;font-size:14px;color:var(--muted)}

/* promo */
.promo-photo{left:0;top:2630px;width:612px;height:479px;background:linear-gradient(90deg,#8a7464 0%,#5b4a3f 30%,#c9c6c2 55%,#7d6a5b 100%)}
.promo{left:612px;top:2630px;width:588px;height:479px;background:var(--gold)}
.promo-title{left:687px;top:2740px;font-size:52px;color:var(--white);line-height:1.1}
.promo-input{left:681px;top:2849px;width:404px;height:64px;border:2px solid var(--white);border-radius:8px;font-size:14px;color:var(--white);padding-left:26px;display:flex;align-items:center}

/* footer */
.chat{left:1073px;top:3147px;width:46px;height:46px;border-radius:50%;background:var(--gold);display:flex;align-items:center;justify-content:center}
.foot-brand{left:111px;top:3282px;display:flex;align-items:center;gap:12px;font-weight:700;font-size:24px;color:var(--ink)}
.foot-brand .mark{width:40px;height:40px;border-radius:50%;background:var(--ink)}
.foot-col h4{font-size:19px;font-weight:700;color:var(--ink);letter-spacing:.3px}
.foot-col .rule{margin-top:10px;width:36px;height:2px}
.foot-col ul{list-style:none;margin-top:30px}
.foot-col li{font-size:14px;line-height:21.4px;color:var(--muted)}
.foot-col li::before{content:"»";margin-right:14px;color:var(--ink)}
.contact-row{display:flex;gap:10px;font-size:14px;line-height:21.4px;color:var(--muted)}
.contact-row svg{flex:none;margin-top:4px}
.divider{left:111px;top:3440px;width:977px;height:1px;background:var(--line)}
.copy{left:0;top:3468px;width:1200px;text-align:center;font-size:14px;color:var(--text)}
.social{left:537px;top:3502px;display:flex;gap:9px}
.social span{width:24px;height:24px;border-radius:50%;background:#9a9a9a}
.pay{left:432px;top:3556px;display:flex;gap:24px}
.pay span{width:36px;height:16px;border-radius:3px;background:#d9d9d9}
</style>
</head>
<body>

<!-- header + hero -->
<div class="abs hero"></div>
<div class="abs hero-photo" role="img" aria-label="Smiling young man wearing a white brand t-shirt against a light grey wall"></div>
<div class="abs brand"><span class="mark"></span>Zip Tribe Gear</div>
<nav class="abs nav">
  <a class="active" href="#">Home</a><a href="#">About us</a><a href="#">Our Product</a><a href="#">Blog</a><a href="#">Contact us</a>
</nav>
<div class="abs cart">
  <span class="ico"><svg width="14" height="12" viewBox="0 0 14 12"><path d="M0 1h2.5l2 7h7l1.5-5H4" fill="none" stroke="#222" stroke-width="1.6"/><circle cx="5.5" cy="10.5" r="1.2" fill="#222"/><circle cx="10.5" cy="10.5" r="1.2" fill="#222"/></svg></span>
  My Cart : $0.00
</div>
<div class="abs login"><svg width="11" height="11" viewBox="0 0 11 11"><circle cx="5.5" cy="3" r="2.6" fill="#222"/><path d="M0 11c0-3.5 2.5-5 5.5-5s5.5 1.5 5.5 5z" fill="#222"/></svg>Login</div>

<h1 class="abs display hero-title">Zip Tribe Gear</h1>
<p class="abs hero-copy">Lorem ipsum dolor sit amet, consectetur adipiscing elit, sed do eiusmod tempor</p>
<div class="abs btn-gold">REQUEST A QUOTE</div>
<div class="abs dots"><span></span><span></span><span></span><span></span></div>

<!-- products -->
<h2 class="abs display sec-title" style="top:788px">Our Product</h2>
<div class="abs rule" style="left:562px;top:863px"></div>

<div class="abs card" style="left:111px">
  <div class="shot" role="img" aria-label="White t-shirt with line-art character print"></div>
  <div class="name">Lorem ipsum dolor sit</div>
  <div class="price">$25.00</div>
  <div class="opt color">COLOR ⌄<span class="swatch"></span></div>
  <div class="opt size">SIZE ⌄<span class="size-box">L</span></div>
  <svg class="corner" viewBox="0 0 56 56"><path d="M56 0V56H0z" fill="#edbb45"/><path d="M32 38h3l2 8h9l2-6H36" fill="none" stroke="#fff" stroke-width="1.8"/><circle cx="38" cy="49" r="1.4" fill="#fff"/><circle cx="45" cy="49" r="1.4" fill="#fff"/></svg>
</div>
<div class="abs card" style="left:444px">
  <div class="shot" role="img" aria-label="White t-shirt with line-art character print"></div>
  <div class="name">Lorem ipsum dolor sit</div>
  <div class="price">$25.00</div>
  <div class="opt color">COLOR ⌄<span class="swatch"></span></div>
  <div class="opt size">SIZE ⌄<span class="size-box">L</span></div>
  <svg class="corner" viewBox="0 0 56 56"><path d="M56 0V56H0z" fill="#edbb45"/><path d="M32 38h3l2 8h9l2-6H36" fill="none" stroke="#fff" stroke-width="1.8"/><circle cx="38" cy="49" r="1.4" fill="#fff"/><circle cx="45" cy="49" r="1.4" fill="#fff"/></svg>
</div>
<div class="abs card" style="left:776px">
  <div class="shot" role="img" aria-label="White t-shirt with line-art character print"></div>
  <div class="name">Lorem ipsum dolor sit</div>
  <div class="price">$25.00</div>
  <div class="opt color">COLOR ⌄<span class="swatch"></span></div>
  <div class="opt size">SIZE ⌄<span class="size-box">L</span></div>
  <svg class="corner" viewBox="0 0 56 56"><path d="M56 0V56H0z" fill="#edbb45"/><path d="M32 38h3l2 8h9l2-6H36" fill="none" stroke="#fff" stroke-width="1.8"/><circle cx="38" cy="49" r="1.4" fill="#fff"/><circle cx="45" cy="49" r="1.4" fill="#fff"/></svg>
</div>

<!-- about -->
<section class="abs about"></section>
<h2 class="abs display about-title">About Us</h2>
<div class="abs rule" style="left:111px;top:1618px;background:#fff"></div>
<p class="abs about-copy">Lorem ipsum dolor sit amet, consectetur adipiscing elit, sed do eiusmod tempor incididunt ut labore et dolore magna aliqua. Ut enim ad minim veniam, quis nostrud exercitation ullamco laboris nisi ut aliquip ex ea commodo consequat. Duis aute irure dolor in reprehenderit in voluptate velit esse cillum dolore eu fugiat nulla pariatur. Excepteur sint occaecat cupidatat non proident, sunt in culpa qui officia deserunt mollit anim id est laborum.</p>
<div class="abs btn-white" style="left:111px;top:1836px;width:141px;height:41px;border-radius:21px">LEARN MORE</div>
<div class="abs about-frame"></div>
<div class="abs about-photo" role="img" aria-label="Flat lay of a white printed t-shirt with jeans, headphones and greenery on wooden boards"></div>

<!-- testimonials -->
<h2 class="abs display sec-title" style="top:2095px">Testimonials</h2>
<div class="abs rule" style="left:562px;top:2170px"></div>
<svg class="abs" style="left:42px;top:2361px" width="24" height="24" viewBox="0 0 24 24"><path d="M21 2 3 12l18 10z" fill="none" stroke="#222" stroke-width="2"/></svg>
<svg class="abs" style="left:1131px;top:2361px" width="24" height="24" viewBox="0 0 24 24"><path d="M3 2l18 10L3 22z" fill="none" stroke="#222" stroke-width="2"/></svg>

<div class="abs quote" style="left:111px"><span class="qm">“</span><span class="stars">★★★★★</span><p class="say">"Lorem ipsum dolor sit amet, consectetur adipiscing elit, sed do eiusmod tempor incidi dunt ut labore et dolore magna aliqua.Lorem ipsum dolor sit amet, consectetur adipiscing elit, sed do eiusmod"</p><span class="avatar" role="img" aria-label="Customer portrait"></span><span class="who">John doe</span><span class="org">Company name</span></div>
<div class="abs quote alt" style="left:358px"><span class="qm">“</span><span class="stars">★★★★★</span><p class="say">"Lorem ipsum dolor sit amet, consectetur adipiscing elit, sed do eiusmod tempor incidi dunt ut labore et dolore magna aliqua.Lorem ipsum dolor sit amet, consectetur adipiscing elit, sed do eiusmod"</p><span class="avatar" role="img" aria-label="Customer portrait"></span><span class="who">John doe</span><span class="org">Company name</span></div>
<div class="abs quote" style="left:606px"><span class="qm">“</span><span class="stars">★★★★★</span><p class="say">"Lorem ipsum dolor sit amet, consectetur adipiscing elit, sed do eiusmod tempor incidi dunt ut labore et dolore magna aliqua.Lorem ipsum dolor sit amet, consectetur adipiscing elit, sed do eiusmod"</p><span class="avatar" role="img" aria-label="Customer portrait"></span><span class="who">John doe</span><span class="org">Company name</span></div>
<div class="abs quote" style="left:853px"><span class="qm">“</span><span class="stars">★★★★★</span><p class="say">"Lorem ipsum dolor sit amet, consectetur adipiscing elit, sed do eiusmod tempor incidi dunt ut labore et dolore magna aliqua.Lorem ipsum dolor sit amet, consectetur adipiscing elit, sed do eiusmod"</p><span class="avatar" role="img" aria-label="Customer portrait"></span><span class="who">John doe</span><span class="org">Company name</span></div>

<!-- promo -->
<div class="abs promo-photo" role="img" aria-label="Bearded man in sunglasses wearing a white printed t-shirt on a city street"></div>
<section class="abs promo"></section>
<h2 class="abs display promo-title">Add A Promo Code</h2>
<div class="abs rule" style="left:687px;top:2816px;background:#fff"></div>
<div class="abs promo-input">FGH5248</div>
<div class="abs btn-white" style="left:686px;top:2931px;width:167px;height:59px;border-radius:6px">APPLY NOW</div>

<!-- footer -->
<div class="abs chat"><svg width="16" height="14" viewBox="0 0 16 14"><ellipse cx="8" cy="6" rx="7" ry="5" fill="#fff"/><path d="M4 9l-2 4 5-3z" fill="#fff"/></svg></div>
<div class="abs foot-brand"><span class="mark"></span>Zip Tribe Gear</div>

<div class="abs foot-col" style="left:384px;top:3211px">
  <h4>QUICK LINKS</h4><div class="rule"></div>
  <ul><li>Home</li><li>About us</li><li>Products</li><li>Latest News</li><li>Recent Clients</li><li>Contact</li></ul>
</div>
<div class="abs foot-col" style="left:641px;top:3211px">
  <h4>INFORMATION</h4><div class="rule"></div>
  <ul><li>Privacy policy</li><li>Terms &amp; condition</li><li>Support</li><li>Faq</li><li>Blog</li><li>Evevnt</li></ul>
</div>
<div class="abs foot-col" style="left:857px;top:3211px;width:260px">
  <h4>CONTACT US</h4><div class="rule"></div>
  <div class="contact-row" style="margin-top:30px"><svg width="11" height="14" viewBox="0 0 11 14"><path d="M5.5 0A5.5 5.5 0 0 0 0 5.5C0 9 5.5 14 5.5 14S11 9 11 5.5A5.5 5.5 0 0 0 5.5 0z" fill="#edbb45"/><circle cx="5.5" cy="5.5" r="2" fill="#fff"/></svg><div><b style="color:#444;font-weight:500">Zip Tribe Gear</b><br>123,Lorem ipsum dolor sit am<br>consectetur</div></div>
  <div class="contact-row" style="margin-top:21px"><svg width="13" height="13" viewBox="0 0 13 13"><path d="M3 0l2 3-1.5 1.5a8 8 0 0 0 5 5L10 8l3 2-1.5 3C6 13 0 7 0 1.5z" fill="#edbb45"/></svg>Phone : +1 888 888 8888</div>
  <div class="contact-row"><svg width="13" height="11" viewBox="0 0 13 11"><rect width="13" height="11" rx="1" fill="#edbb45"/><path d="M0 1l6.5 5L13 1" fill="none" stroke="#fff" stroke-width="1.3"/></svg>Email : info@ziptribegear.com</div>
</div>

<div class="abs divider"></div>
<p class="abs copy">Copyright 2022 Company name | All Rights Reserved</p>
<div class="abs social"><span></span><span></span><span></span><span></span></div>
<div class="abs pay"><span></span><span></span><span></span><span></span><span></span><span></span></div>

</body>
</html>
```